Landing Page IT Security Vendor

We need a landing page that uses our colour scheme (www.veldonguard.com). We created a draft (see attached). We do not need standard stock template design pages. Please only apply if you can design pages from scratch and try to be as close as possible to our draft. It is ok to also purchase commecrial stock pictures

Coding

Coded - Design and coding required

Number of Pages Required

1 page

```html
<!DOCTYPE html>
<html lang="en">
<head>
<meta charset="utf-8">
<title>Veldon Guard – Security Awareness Training</title>
<link href="https://fonts.googleapis.com/css2?family=Raleway:wght@400;500;600;700&display=swap" rel="stylesheet">
<style>
:root{
  --teal:#17b3bf;
  --orange:#f7a01a;
  --dark:#363636;
  --darker:#2b2b2b;
  --ink:#2a2a2a;
  --muted:#555;
  --light:#f4f5f7;
  --white:#fff;
}
*{margin:0;padding:0;box-sizing:border-box}
html,body{width:1200px;height:3116px;overflow:hidden}
body{position:relative;font-family:'Raleway',sans-serif;color:var(--ink);background:var(--white)}
.abs{position:absolute}

/* header */
.site-header{left:0;top:0;width:1200px;height:94px;background:var(--white)}
.brand{left:160px;top:30px;display:flex;align-items:center;gap:10px}
.brand-mark{width:26px;height:26px;border-radius:50%;background:var(--orange)}
.brand-name{font-weight:700;font-size:24px;color:var(--ink)}
.lang{left:290px;top:48px;font-size:13px;color:#888}
.nav-home{left:854px;top:35px;width:92px;height:34px;border-radius:17px;background:var(--teal);color:#fff;font-size:15px;font-weight:500;display:flex;align-items:center;justify-content:center}
.nav-solution{left:968px;top:43px;font-size:15px;color:var(--ink);font-weight:500}

/* hero */
.hero{left:0;top:94px;width:1200px;height:627px;background:radial-gradient(ellipse at 50% 45%,#8a4f8f 0%,#3b2f5e 35%,#171b33 70%,#0e1020 100%)}
.hero-photo{left:0;top:0;width:1200px;height:627px}
.hero-title{left:0;top:352px;width:1200px;text-align:center;color:#fff;font-size:40px;font-weight:700}
.hero-title span{font-weight:500}
.hero-sub{left:0;top:416px;width:1200px;text-align:center;color:#fff;font-size:25px;font-weight:500}
.btn{display:flex;align-items:center;justify-content:center;border-radius:24px;font-size:12px;font-weight:600;text-transform:uppercase}
.btn-outline{left:432px;top:478px;width:160px;height:44px;border:2px solid #fff;color:#fff}
.btn-solid{left:607px;top:478px;width:162px;height:44px;background:#fff;color:#1e2a6b}

/* help */
.help{left:0;top:721px;width:1200px;height:1161px;background:var(--light)}
.help-curve{left:0;top:0;width:1200px;height:1161px}
.help-title{left:0;top:95px;width:1200px;text-align:center;font-size:44px;font-weight:700;color:var(--ink)}
.card{width:270px;height:520px;top:207px;background:#fff;box-shadow:0 6px 20px rgba(0,0,0,.08)}
.card-top{left:0;top:0;width:270px;height:210px;border-radius:135px 135px 0 0}
.card-top.c1{background:linear-gradient(160deg,#3d5a78,#16273e)}
.card-top.c2{background:linear-gradient(160deg,#25509a,#0d1f4b)}
.card-top.c3{background:linear-gradient(160deg,#3a4551,#121820)}
.card-cap{left:30px;top:65px;width:210px;text-align:center;color:#fff;font-size:16px;line-height:20px;font-weight:500}
.card-icon{left:69px;top:136px;width:132px;height:132px;border-radius:50%;background:#fff;display:flex;align-items:center;justify-content:center}
.card-lead{left:20px;top:280px;width:230px;text-align:center;font-size:16.5px;line-height:22px;font-weight:500}
.card-body{left:30px;top:390px;width:210px;text-align:center;font-size:13px;line-height:19.5px;color:var(--muted)}
.card-btn{left:45px;top:470px;width:180px;height:30px;border-radius:15px;color:#fff;font-size:11.5px;display:flex;align-items:center;justify-content:center;font-weight:500;text-transform:uppercase}
.card-btn.dark{background:#2f2f2f}
.card-btn.accent{background:var(--orange)}

.mssp-title{left:158px;top:843px;width:520px;color:#fff;font-size:45px;line-height:61px;font-weight:700}
.mssp-text{left:158px;top:976px;width:460px;color:#e8e8e8;font-size:15px;line-height:22.5px}
.btn-learn{left:750px;top:921px;width:184px;height:50px;border-radius:25px;background:var(--orange);color:#fff;font-size:16px;font-weight:500;text-transform:uppercase}

/* trust */
.trust{left:0;top:1882px;width:1200px;height:495px;background:linear-gradient(90deg,#f6f7f9,#eef0f3)}
.trust-photo{left:698px;top:0;width:502px;height:495px;background:linear-gradient(180deg,#b7c7d4 0%,#8fa1b0 45%,#4e5a66 100%)}
.trust-title{left:158px;top:44px;width:520px;font-size:35px;line-height:42px;color:#333}
.trust-title b{color:var(--teal);font-weight:700}
.trust-text{left:158px;top:192px;width:490px;font-size:16px;line-height:24px;color:#444}
.trust-sub{left:158px;top:288px;font-size:19px;font-weight:600;color:#222}
.trust-small{left:158px;top:324px;width:490px;font-size:14.5px;line-height:24px;color:#444}
.btn-contact{left:161px;top:386px;width:184px;height:43px;border-radius:22px;background:var(--orange);color:#fff;font-size:14px;font-weight:500;text-transform:uppercase}

/* clients */
.clients{left:188px;top:2443px;width:824px;height:200px}
.client{position:absolute;display:flex;align-items:center;justify-content:center;gap:8px;font-size:22px;font-weight:700;color:#333}
.client .sq{width:18px;height:18px;background:#333}
.client .dot{width:18px;height:18px;border-radius:50%;background:#333}
.grid-v{position:absolute;width:1px;background:#ddd}
.grid-h{position:absolute;height:1px;background:#ddd}

/* footer */
.footer{left:0;top:2716px;width:1200px;height:400px;background:var(--teal);color:#fff}
.f-head{font-size:18px;font-weight:600}
.f-line{font-size:15px;line-height:24px}
.f-row{display:flex;gap:10px;align-items:flex-start}
.f-div{width:1px;background:rgba(255,255,255,.5)}
.f-rule{left:160px;top:278px;width:880px;height:1px;background:rgba(255,255,255,.7)}
.badges{left:332px;top:305px;display:flex;gap:13px;align-items:center}
.badge{background:rgba(255,255,255,.85)}
</style>
</head>
<body>

<header class="site-header abs">
  <div class="brand abs"><span class="brand-mark"></span><span class="brand-name">Veldon</span></div>
  <div class="lang abs">English</div>
  <div class="nav-home abs">Home</div>
  <div class="nav-solution abs">Solution
    <svg width="10" height="7" viewBox="0 0 10 7"><path d="M1 1l4 4 4-4" fill="none" stroke="#888" stroke-width="1.3"/></svg>
  </div>
</header>

<section class="hero abs">
  <div class="hero-photo abs" role="img" aria-label="Businessman standing before the globe at night with a glowing network of connected people icons"></div>
  <h1 class="hero-title abs">Train Your Staff <span>&nbsp;With</span> Veldon</h1>
  <p class="hero-sub abs">And Improve Cyber Security Awareness</p>
  <a class="btn btn-outline abs">Download Veldon</a>
  <a class="btn btn-solid abs">Request a Demo</a>
</section>

<section class="help abs">
  <svg class="help-curve abs" viewBox="0 0 1200 1161" preserveAspectRatio="none">
    <path d="M0 640 C 250 470, 700 430, 1200 530 L1200 1161 L0 1161 Z" fill="#363636"/>
  </svg>
  <h2 class="help-title abs">How Can We Help?</h2>

  <div class="card abs" style="left:157px">
    <div class="card-top c1 abs" role="img" aria-label="Businessman touching a digital interface"></div>
    <div class="card-cap abs">Import our training courses in your LMS</div>
    <div class="card-icon abs">
      <svg width="86" height="86" viewBox="0 0 86 86"><path d="M43 8 L78 22 L43 36 L8 22 Z" fill="#17b3bf"/><path d="M22 30 v14 c0 6 42 6 42 0 v-14 l-21 8 z" fill="#17b3bf"/><rect x="10" y="52" width="8" height="26" fill="#17b3bf"/><path d="M22 56 h28 c6 0 6 8 0 8 h-14 h18 l20-10 c6-2 8 4 4 8 l-22 14 h-34 z" fill="#17b3bf"/></svg>
    </div>
    <div class="card-lead abs">Buy out of the box or courses you can import in your elearning</div>
    <div class="card-body abs" style="top:358px">Veldon offers 250 fully customizable training modules in +30 Languages. Games, Videos, Exams, Posters,Offline, Micro-training and much more!</div>
    <div class="card-btn dark abs">Explore our training</div>
  </div>

  <div class="card abs" style="left:465px">
    <div class="card-top c2 abs" role="img" aria-label="Blue digital security shield background"></div>
    <div class="card-cap abs" style="top:58px">Let us develop a security awareness program</div>
    <div class="card-icon abs">
      <svg width="86" height="86" viewBox="0 0 86 86"><path d="M43 4 L74 16 V40 C74 60 60 74 43 82 C26 74 12 60 12 40 V16 Z" fill="#17b3bf"/><circle cx="43" cy="42" r="17" fill="none" stroke="#fff" stroke-width="5"/><path d="M35 42 l6 6 l11-11" fill="none" stroke="#fff" stroke-width="5"/></svg>
    </div>
    <div class="card-lead abs">Veldon security will assist you inimproving security awareness with money back guarantee!</div>
    <div class="card-body abs" style="top:378px">Lorem Ipsum is simply dummy text of the printing and typesetting industry.</div>
    <div class="card-btn accent abs">Explore our training</div>
  </div>

  <div class="card abs" style="left:768px">
    <div class="card-top c3 abs" role="img" aria-label="Hands typing on a laptop keyboard"></div>
    <div class="card-cap abs" style="top:58px">Install the Veldon software on pemiseor get access to the saas vetsion</div>
    <div class="card-icon abs">
      <svg width="86" height="86" viewBox="0 0 86 86"><rect x="36" y="4" width="14" height="26" fill="#17b3bf"/><path d="M24 28 h38 l-19 20 z" fill="#17b3bf"/><path d="M6 52 L43 36 L80 52 L43 68 Z" fill="#17b3bf"/><path d="M6 62 L43 78 L80 62 L80 68 L43 84 L6 68 Z" fill="#17b3bf"/></svg>
    </div>
    <div class="card-lead abs">You want to run the campaign yourself? Choose your perfered setup type and get started in 24h!</div>
    <div class="card-body abs" style="top:378px">Lorem Ipsum is simply dummy text of the printing and typesetting industry. Lorem Ipsum</div>
    <div class="card-btn dark abs">Explore our training</div>
  </div>

  <h2 class="mssp-title abs">Veldon Is Also AvailAble For MSSP</h2>
  <p class="mssp-text abs">Lorem ipsum dolor sit amet, consectetur adipiscing elit, sed do eiusmod tempor incididunt ut labore et dolore magna aliqua. Ut enim ad minim veniam, quis nostrud exercitation</p>
  <a class="btn btn-learn abs">Learn More</a>
</section>

<section class="trust abs">
  <div class="trust-photo abs" role="img" aria-label="Diverse group of smiling colleagues in a bright office"></div>
  <h2 class="trust-title abs">Already <b>over 12'000'000 Employees</b> worldwide trust and use VELDON</h2>
  <p class="trust-text abs">Veldon Guard is a name you can trust! Because we have won countless awards since 2015 and help wellknown brands around the world.</p>
  <p class="trust-sub abs">You know you're getting a quality solution with us.</p>
  <p class="trust-small abs">Our services can be customized to fit your needs and copany size. Talk to our team today to learn more</p>
  <a class="btn btn-contact abs">Contact with us</a>
</section>

<section class="clients abs">
  <div class="grid-v" style="left:199px;top:0;height:200px"></div>
  <div class="grid-v" style="left:412px;top:0;height:200px"></div>
  <div class="grid-v" style="left:625px;top:0;height:200px"></div>
  <div class="grid-h" style="left:0;top:100px;width:824px"></div>
  <div class="client" style="left:0;top:0;width:199px;height:100px"><span class="sq"></span>Arvonia</div>
  <div class="client" style="left:199px;top:0;width:213px;height:100px">Nordbahn</div>
  <div class="client" style="left:412px;top:0;width:213px;height:100px"><span class="sq"></span>Casalia</div>
  <div class="client" style="left:625px;top:0;width:199px;height:100px">Brenner</div>
  <div class="client" style="left:0;top:100px;width:199px;height:100px">Altura</div>
  <div class="client" style="left:199px;top:100px;width:213px;height:100px">Verant</div>
  <div class="client" style="left:412px;top:100px;width:213px;height:100px"><span class="dot"></span>Kessler</div>
  <div class="client" style="left:625px;top:100px;width:199px;height:100px;font-size:18px">Stadtwerk Ost</div>
</section>

<footer class="footer abs">
  <div class="abs f-head" style="left:162px;top:58px">Contact Us</div>
  <div class="abs f-row" style="left:162px;top:98px">
    <svg width="14" height="18" viewBox="0 0 14 18"><path d="M7 0C3 0 0 3 0 7c0 5 7 11 7 11s7-6 7-11c0-4-3-7-7-7z" fill="#fff"/><circle cx="7" cy="7" r="2.5" fill="#17b3bf"/></svg>
    <div class="f-line">Urope Veldon Guard AG<br>Seeweg 12 | 6010 Brunnen<br>Switzerland</div>
  </div>
  <div class="abs f-head" style="left:160px;top:196px">Language</div>
  <div class="abs f-line" style="left:161px;top:228px;font-size:14px">English
    <svg width="10" height="7" viewBox="0 0 10 7"><path d="M1 1l4 4 4-4" fill="none" stroke="#fff" stroke-width="1.3"/></svg></div>

  <div class="abs f-div" style="left:417px;top:60px;height:160px"></div>
  <div class="abs f-head" style="left:472px;top:58px">Address</div>
  <div class="abs f-row" style="left:472px;top:98px">
    <svg width="14" height="18" viewBox="0 0 14 18"><path d="M7 0C3 0 0 3 0 7c0 5 7 11 7 11s7-6 7-11c0-4-3-7-7-7z" fill="#fff"/><circle cx="7" cy="7" r="2.5" fill="#17b3bf"/></svg>
    <div class="f-line">North America<br>Veldon Guard USA<br>4420 Harbor Park Dr Suite 210<br>Denton, TX 76201</div>
  </div>

  <div class="abs f-div" style="left:756px;top:60px;height:160px"></div>
  <div class="abs f-head" style="left:807px;top:58px">Phone</div>
  <div class="abs" style="left:803px;top:96px">
    <div class="f-row" style="margin-bottom:14px"><svg width="16" height="16" viewBox="0 0 16 16"><path d="M3 1l3 3-2 2c1 2 3 4 5 5l2-2 3 3-2 3C6 15 1 10 1 3z" fill="#fff"/></svg><span class="f-line">Global: +41 44 000 12 34</span></div>
    <div class="f-row" style="margin-bottom:14px"><svg width="16" height="16" viewBox="0 0 16 16"><path d="M3 1l3 3-2 2c1 2 3 4 5 5l2-2 3 3-2 3C6 15 1 10 1 3z" fill="#fff"/></svg><span class="f-line">USA: +1 555 010 2030</span></div>
    <div class="f-row" style="margin-bottom:14px"><svg width="16" height="16" viewBox="0 0 16 16"><path d="M3 1l3 3-2 2c1 2 3 4 5 5l2-2 3 3-2 3C6 15 1 10 1 3z" fill="#fff"/></svg><span class="f-line">USA Support: +1 555 010 2040</span></div>
    <div class="f-row"><svg width="16" height="16" viewBox="0 0 16 16"><path d="M3 1l3 3-2 2c1 2 3 4 5 5l2-2 3 3-2 3C6 15 1 10 1 3z" fill="#fff"/></svg><span class="f-line">France: +33 600 000 123</span></div>
  </div>

  <div class="f-rule abs"></div>
  <div class="abs" style="left:172px;top:312px;display:flex;align-items:center;gap:6px">
    <span style="width:14px;height:14px;border-radius:50%;background:var(--orange)"></span>
    <span style="font-weight:700;font-size:14px;color:#fff">Veldon</span>
  </div>
  <div class="abs" style="left:171px;top:346px;font-size:11px">All Rights Reserved 2020</div>
  <div class="badges abs">
    <div class="badge" style="width:60px;height:56px;border-radius:6px"></div>
    <div class="badge" style="width:54px;height:54px;border-radius:50%"></div>
    <div class="badge" style="width:40px;height:54px;border-radius:4px"></div>
    <div class="badge" style="width:40px;height:54px;border-radius:4px"></div>
    <div class="badge" style="width:44px;height:54px;border-radius:4px"></div>
    <div class="badge" style="width:60px;height:34px;border-radius:4px"></div>
    <div class="badge" style="width:44px;height:54px;border-radius:4px"></div>
    <div class="badge" style="width:50px;height:50px;border-radius:4px"></div>
    <div class="badge" style="width:80px;height:34px;border-radius:17px"></div>
    <div class="badge" style="width:54px;height:54px;border-radius:50%"></div>
  </div>
</footer>

</body>
</html>
```